CPA Firm Business Card
Halvorin, Bestwick & Pardue CPAs, LLC
Project: CPA Firm Business Card
CPA Firm Business Card - Financial Services
Creative Brief
Professional
Moss Brandley, CPA
2867 E. Sable Way, Suite 348 Tucson, AZ 85619
moss@quillledger.net
In addition to business cards design I would also like to see designs for letterheads, envelopes and fax cover sheets.

```html
<!DOCTYPE html>
<html lang="en">
<head>
<meta charset="utf-8">
<title>Halvorin, Bestwick &amp; Pardue CPAs, LLC — Stationery Set</title>
<link rel="stylesheet" href="https://fonts.googleapis.com/css2?family=Roboto+Condensed:wght@400;700&display=swap">
<style>
  :root {
    --maroon: #7b1116;
    --maroon-dark: #5f0c10;
    --swoosh-grey: #8c8c8c;
    --paper: #ffffff;
    --ink: #4a4a4a;
    --faint: #f1e4e5;
    --stage: #e4e1dd;
  }
  * { box-sizing: border-box; margin: 0; padding: 0; }
  html, body { width: 1200px; height: 904px; overflow: hidden; }
  body {
    background: var(--stage);
    font-family: "Roboto Condensed", sans-serif;
    position: relative;
  }
  .piece {
    position: absolute;
    background: var(--paper);
    overflow: hidden;
    box-shadow: 0 2px 6px rgba(0,0,0,.18);
  }
  .piece > svg.shape { position: absolute; inset: 0; width: 100%; height: 100%; }
  .brand {
    position: absolute;
    display: flex;
    align-items: flex-start;
    gap: 5px;
    color: var(--maroon);
    font-weight: 700;
    text-transform: uppercase;
    line-height: 1.05;
  }
  .brand-mark { background: var(--maroon); flex: none; }
  .contact {
    position: absolute;
    color: var(--paper);
    line-height: 1.45;
  }
  .contact.dark { color: var(--ink); }

  /* letterheads */
  .letterhead { width: 289px; height: 377px; top: 44px; }
  .letterhead.first { left: 171px; }
  .letterhead.second { left: 492px; }
  .letterhead .brand { top: 14px; left: 14px; font-size: 9px; }
  .letterhead .brand-mark { width: 12px; height: 12px; }
  .letterhead .faint-name {
    position: absolute; top: 160px; left: 0; right: 0;
    text-align: center; color: var(--faint);
    font-size: 22px; font-weight: 700; text-transform: uppercase; line-height: 1.1;
  }
  .letterhead .contact { right: 14px; bottom: 10px; font-size: 5px; text-align: left; width: 62px; }

  /* envelopes */
  .envelope { left: 803px; width: 348px; }
  .envelope.front { top: 44px; height: 152px; }
  .envelope.front .brand { top: 12px; left: 12px; font-size: 8px; }
  .envelope.front .brand-mark { width: 10px; height: 10px; }
  .envelope.front .return-line { position: absolute; top: 40px; left: 12px; font-size: 5px; color: var(--ink); }
  .envelope.back { top: 208px; height: 213px; background: transparent; box-shadow: none; }

  /* folder */
  .folder { left: 157px; top: 448px; width: 649px; height: 421px; background: var(--maroon); }
  .folder .spine { position: absolute; left: 324px; top: 0; bottom: 0; width: 1px; background: rgba(0,0,0,.25); }
  .folder .back-label {
    position: absolute; left: 108px; top: 193px; width: 118px; height: 32px;
    background: var(--paper); padding: 5px 6px;
  }
  .folder .back-label .brand { position: static; font-size: 7px; }
  .folder .back-label .brand-mark { width: 9px; height: 9px; }
  .folder .front-brand { top: 76px; left: 392px; font-size: 19px; gap: 9px; }
  .folder .front-brand .brand-mark { width: 26px; height: 26px; }
  .folder .address { left: 18px; bottom: 14px; font-size: 6px; }
  .folder .web { left: 440px; bottom: 18px; font-size: 6px; letter-spacing: 1px; }

  /* business cards */
  .card-large { left: 857px; top: 490px; width: 294px; height: 118px; }
  .card-large .brand { top: 12px; left: 160px; font-size: 8px; }
  .card-large .brand-mark { width: 11px; height: 11px; }
  .card-large .contact.dark { left: 12px; top: 40px; font-size: 5.5px; }
  .card-large .holder { position: absolute; right: 12px; bottom: 10px; color: var(--paper); font-size: 8px; font-weight: 700; }

  .card-small { left: 34px; width: 120px; height: 69px; border-radius: 6px; }
  .card-small.front { top: 154px; }
  .card-small.back { top: 240px; }
  .card-small .brand { font-size: 4.5px; gap: 3px; }
  .card-small .brand-mark { width: 6px; height: 6px; }
  .card-small.front .brand { top: 7px; left: 7px; }
  .card-small.back .brand { top: 26px; left: 58px; }
  .card-small .contact.dark { left: 7px; top: 25px; font-size: 3.5px; }
</style>
</head>
<body>

<!-- Letterhead, first sheet -->
<section class="piece letterhead first">
  <svg class="shape" viewBox="0 0 289 377" preserveAspectRatio="none" aria-hidden="true">
    <path d="M0 342 Q160 326 289 276 L289 286 Q160 334 0 348 Z" fill="var(--swoosh-grey)"/>
    <path d="M0 350 Q160 336 289 288 L289 377 L0 377 Z" fill="var(--maroon)"/>
  </svg>
  <div class="brand"><span class="brand-mark"></span><span>Halvorin, Bestwick<br>&amp; Pardue<br>CPAs, LLC</span></div>
  <div class="faint-name">Halvorin<br>Bestwick<br>&amp; Pardue</div>
  <div class="contact">2867 E. Sable Way, Suite 348<br>Tucson, AZ 85619<br>T (520) 555-0148<br>F (520) 555-0149<br>www.quillledger.net</div>
</section>

<!-- Letterhead, second sheet -->
<section class="piece letterhead second">
  <svg class="shape" viewBox="0 0 289 377" preserveAspectRatio="none" aria-hidden="true">
    <path d="M0 342 Q160 326 289 276 L289 286 Q160 334 0 348 Z" fill="var(--swoosh-grey)"/>
    <path d="M0 350 Q160 336 289 288 L289 377 L0 377 Z" fill="var(--maroon)"/>
  </svg>
  <div class="brand"><span class="brand-mark"></span><span>Halvorin, Bestwick<br>&amp; Pardue<br>CPAs, LLC</span></div>
  <div class="faint-name">Halvorin<br>Bestwick<br>&amp; Pardue</div>
  <div class="contact">2867 E. Sable Way, Suite 348<br>Tucson, AZ 85619<br>T (520) 555-0148<br>F (520) 555-0149<br>www.quillledger.net</div>
</section>

<!-- Envelope, front -->
<section class="piece envelope front">
  <svg class="shape" viewBox="0 0 348 152" preserveAspectRatio="none" aria-hidden="true">
    <path d="M0 118 Q190 110 348 58 L348 66 Q190 118 0 124 Z" fill="var(--swoosh-grey)"/>
    <path d="M0 126 Q190 120 348 68 L348 152 L0 152 Z" fill="var(--maroon)"/>
  </svg>
  <div class="brand"><span class="brand-mark"></span><span>Halvorin, Bestwick &amp; Pardue CPAs, LLC</span></div>
  <div class="return-line">2867 E. Sable Way, Suite 348 · Tucson, AZ 85619</div>
</section>

<!-- Envelope, back with open flap -->
<section class="piece envelope back">
  <svg class="shape" viewBox="0 0 348 213" preserveAspectRatio="none" aria-hidden="true">
    <path d="M0 0 L174 36 L348 0 L348 40 L0 40 Z" fill="var(--maroon)"/>
    <path d="M0 0 L174 36 L348 0" fill="none" stroke="var(--maroon-dark)" stroke-width="1"/>
    <rect x="0" y="40" width="348" height="173" fill="var(--paper)"/>
    <path d="M0 40 L150 135 M348 40 L198 135 M0 213 L160 120 L188 120 L348 213" fill="none" stroke="#d8d8d8" stroke-width="1"/>
  </svg>
</section>

<!-- Presentation folder -->
<section class="piece folder">
  <svg class="shape" viewBox="0 0 649 421" preserveAspectRatio="none" aria-hidden="true">
    <path d="M324 0 H649 V252 Q500 214 324 196 Z" fill="var(--paper)"/>
    <path d="M324 196 Q500 214 649 252 L649 262 Q500 224 324 204 Z" fill="var(--swoosh-grey)"/>
  </svg>
  <div class="spine"></div>
  <div class="back-label">
    <div class="brand"><span class="brand-mark"></span><span>Halvorin, Bestwick<br>&amp; Pardue CPAs, LLC</span></div>
  </div>
  <div class="brand front-brand"><span class="brand-mark"></span><span>Halvorin<br>Bestwick &amp;<br>Pardue CPAs, LLC</span></div>
  <div class="contact address">2867 E. Sable Way, Suite 348<br>Tucson, AZ 85619<br>T (520) 555-0148<br>F (520) 555-0149</div>
  <div class="contact web">www.quillledger.net</div>
</section>

<!-- Business card, large view -->
<section class="piece card-large">
  <svg class="shape" viewBox="0 0 294 118" preserveAspectRatio="none" aria-hidden="true">
    <path d="M0 84 Q150 80 294 38 L294 46 Q150 88 0 90 Z" fill="var(--swoosh-grey)"/>
    <path d="M0 92 Q150 90 294 48 L294 118 L0 118 Z" fill="var(--maroon)"/>
  </svg>
  <div class="brand"><span class="brand-mark"></span><span>Halvorin, Bestwick<br>&amp; Pardue CPAs, LLC</span></div>
  <div class="contact dark">T (520) 555-0148<br>F (520) 555-0149<br>moss@quillledger.net</div>
  <div class="holder">Moss Brandley, CPA</div>
</section>

<!-- Business card, small front -->
<section class="piece card-small front">
  <svg class="shape" viewBox="0 0 120 69" preserveAspectRatio="none" aria-hidden="true">
    <path d="M0 50 Q60 48 120 28 L120 32 Q60 52 0 53 Z" fill="var(--swoosh-grey)"/>
    <path d="M0 54 Q60 53 120 33 L120 69 L0 69 Z" fill="var(--maroon)"/>
  </svg>
  <div class="brand"><span class="brand-mark"></span><span>Halvorin, Bestwick<br>&amp; Pardue CPAs</span></div>
  <div class="contact dark">Moss Brandley, CPA<br>moss@quillledger.net</div>
</section>

<!-- Business card, small back -->
<section class="piece card-small back">
  <svg class="shape" viewBox="0 0 120 69" preserveAspectRatio="none" aria-hidden="true">
    <path d="M0 56 Q60 55 120 42 L120 45 Q60 58 0 59 Z" fill="var(--swoosh-grey)"/>
    <path d="M0 60 Q60 59 120 46 L120 69 L0 69 Z" fill="var(--maroon)"/>
  </svg>
  <div class="brand"><span class="brand-mark"></span><span>Halvorin, Bestwick<br>&amp; Pardue CPAs</span></div>
</section>

</body>
</html>
```